Copyright Registration Service Website

Brightvaultly.com (site can be accessed) is a website that will enable artists, photographers, writers, sculptors, musicians and other creative persons of all media to register their works of authorship with the U.S. Ashgrove National Repository, Merriton Bureau, for a nominal fee of $99 plus filing fees (in most cases). The high points of marketing are (1) every application is reviewed by a lawyer and (2) the entire copyright process is monitored, as part of the service fee. There are 8 categories of copyrightability:
Literary Works
Dramatic Works
Musical Works
Sound Recordings
Motion Pictures
Choreographic and Pantomime Works
Photographs, Paintings and Sculptures
Architectural Works
Please look at the existing site; provide a better landing page than currently exists. In particular, the logo is in need of serious improvement. We would like it to be bright and sunny; visually pleasant and witty; and clever but not "doctoral" in presentation. Thank you for your participation.

Target Market(s)

photographers, artists, musicians, age groups of 20-50

Industry/Entity Type

Marketing

Requirements
Should not have
• stiffness

```html
<!DOCTYPE html>
<html lang="en">
<head>
<meta charset="utf-8">
<title>Brightvaultly.com – Copyright Registration</title>
<link href="https://fonts.googleapis.com/css2?family=Open+Sans:wght@400;600;700&display=swap" rel="stylesheet">
<style>
:root{
  --page:#f9f9f9;
  --blue:#0a6fc9;
  --blue-dark:#0558a8;
  --ink:#2a2a2a;
  --muted:#666;
  --hero-bg:#e6e8ea;
  --search:#ececec;
  --white:#fff;
}
*{box-sizing:border-box;margin:0;padding:0}
html,body{width:1177px;height:1200px;overflow:hidden;background:var(--page);font-family:"Open Sans",Arial,sans-serif;color:var(--ink)}
.canvas{position:relative;width:1177px;height:1200px}
.brand{position:absolute;left:131px;top:44px;display:flex;align-items:center;gap:10px}
.brand-dot{width:60px;height:60px;border-radius:50%;border:3px solid #222;background:var(--white)}
.brand-text{display:flex;flex-direction:column;align-items:flex-end}
.brand-name{font-size:25px;font-weight:700;color:#222;letter-spacing:.3px;line-height:1}
.brand-url{font-size:11.5px;font-weight:400;color:#444;margin-top:8px;letter-spacing:.3px}
.account{position:absolute;right:128px;top:30px;text-align:right;font-size:12px}
.account .welcome{color:#111}
.account .links{color:var(--muted);margin-top:5px;letter-spacing:.2px}
.account .links span{margin:0 6px;color:#999}
.search{position:absolute;right:128px;top:78px;width:198px;height:28px;background:var(--search);border-radius:3px;font-size:10px;color:#999;padding:8px 11px}
.nav{position:absolute;left:127px;top:119px;width:923px;height:58px;background:var(--blue);border-radius:3px;display:flex;align-items:center;padding-left:36px;gap:38px}
.nav a{color:var(--white);text-decoration:none;font-size:13.5px;font-weight:600;letter-spacing:.1px}
.hero{position:absolute;left:127px;top:189px;width:923px;height:351px;background:var(--hero-bg);border-radius:3px;overflow:hidden}
.hero-photo{position:absolute;left:0;top:0;width:590px;height:351px;background:linear-gradient(90deg,#cfd3d6 0%,#e4e6e7 40%,#eef0f1 70%,var(--hero-bg) 100%)}
.hero-copy{position:absolute;left:593px;top:94px}
.hero-copy .kicker{font-size:15.5px;color:#222}
.hero-copy h1{font-size:22.5px;font-weight:600;color:#222;margin-top:5px;letter-spacing:.2px}
.hero-copy .price{font-size:26px;font-weight:600;color:var(--blue);margin-top:2px}
.hero-copy .note{font-size:17.5px;color:#333;margin-top:2px}
.btn{display:inline-block;margin-top:27px;width:118px;height:41px;background:linear-gradient(var(--blue),var(--blue-dark));color:var(--white);font-size:11.5px;font-weight:600;text-align:center;line-height:41px;border-radius:2px}
.dots{position:absolute;left:822px;top:296px;display:flex;gap:4px}
.dots i{width:14px;height:14px;border-radius:50%;background:var(--white)}
.dots i.on{background:var(--blue)}
.services-title{position:absolute;left:0;width:1147px;top:562px;text-align:center;font-size:14.5px;font-weight:700;color:var(--blue)}
.tile{position:absolute;width:216px;height:121px;border-radius:3px;overflow:hidden}
.tile span{position:absolute;left:9px;bottom:16px;color:var(--white);font-size:13.5px;font-weight:600;line-height:19px;text-shadow:0 1px 2px #000,0 0 3px #000}
.t1{background:linear-gradient(135deg,#7a4a28,#b98a4a,#3e5a3c)}
.t2{background:linear-gradient(135deg,#8c826c,#b2a78d,#4d4637)}
.t3{background:linear-gradient(135deg,#5a1d6e,#c02b9a,#230c28)}
.t4{background:linear-gradient(135deg,#0e0e10,#2a2c30,#121214)}
.t5{background:linear-gradient(135deg,#dfe3e8,#5c6a80,#1a1f2a)}
.t6{background:linear-gradient(135deg,#3a3a3a,#cfcfcf,#1e1e1e)}
.t7{background:linear-gradient(135deg,#1e2a44,#596d8a,#1b2436)}
.t8{background:linear-gradient(180deg,#28306a,#5f6aa8,#2a2840)}
.pledge{position:absolute;left:0;width:1177px;top:893px;text-align:center;font-size:13.5px;font-weight:700;color:#333}
.pledge-sub{position:absolute;left:0;width:1177px;top:922px;text-align:center;font-size:13.5px;font-weight:700;color:var(--blue)}
.feature{position:absolute;top:982px;width:220px}
.feature h3{display:flex;align-items:center;gap:10px;font-size:13.5px;font-weight:700;color:#222;height:24px}
.feature svg{flex:none}
.feature p{margin-top:17px;font-size:12px;color:#555;line-height:19.5px}
.footer{position:absolute;left:0;top:1127px;width:1177px;height:73px;background:var(--blue);color:var(--white)}
.footer .links{position:absolute;left:130px;top:14px;font-size:12px}
.footer .links span{margin:0 6px}
.footer .copy{position:absolute;left:130px;top:45px;font-size:12px}
.social{position:absolute;left:996px;top:28px;display:flex;gap:7px}
.social i{width:23px;height:23px;border-radius:50%;background:var(--white)}
</style>
</head>
<body>
<div class="canvas">
  <div class="brand">
    <div class="brand-dot"></div>
    <div class="brand-text">
      <div class="brand-name">BRIGHTVAULTLY</div>
      <div class="brand-url">BRIGHTVAULTLY.COM</div>
    </div>
  </div>
  <div class="account">
    <div class="welcome">Welcome Brightvaultly!</div>
    <div class="links">MY ACCOUNT<span>|</span>LOG IN</div>
  </div>
  <div class="search">Search</div>

  <nav class="nav">
    <a>ABOUT US</a><a>COPYRIGHT CATEGORIES</a><a>LAW &amp; STATUES</a><a>COPYRIGHT PROCESS</a><a>CONTACT US</a><a>LINKS</a>
  </nav>

  <section class="hero">
    <div class="hero-photo" role="img" aria-label="Woman in a blue shirt smiling while using a laptop on a white armchair"></div>
    <div class="hero-copy">
      <div class="kicker">Protect your copyright in 5 minutes!</div>
      <h1>COPYRIGHT REGISTRATION</h1>
      <div class="price">$99 (MOST CASES)</div>
      <div class="note">Entire process is reviewed by a lawyer</div>
      <div class="btn">LEARN MORE</div>
    </div>
    <div class="dots"><i class="on"></i><i></i><i></i><i></i></div>
  </section>

  <div class="services-title">Our Services</div>
  <div class="tile t1" style="left:127px;top:600px" role="img" aria-label="Shelves of books"><span>Literary Works</span></div>
  <div class="tile t2" style="left:364px;top:600px" role="img" aria-label="Engraving of a theatrical scene"><span>Dramatic Works</span></div>
  <div class="tile t3" style="left:599px;top:600px" role="img" aria-label="Microphone before a concert stage"><span>Musical Works</span></div>
  <div class="tile t4" style="left:834px;top:600px" role="img" aria-label="Studio microphone in the dark"><span>Sound Recordings</span></div>
  <div class="tile t5" style="left:127px;top:740px" role="img" aria-label="Cyclist in motion"><span>Motion Pictures</span></div>
  <div class="tile t6" style="left:364px;top:740px" role="img" aria-label="Dancers silhouetted on a lit stage"><span>Choreographic &amp;<br>Pantomime Works</span></div>
  <div class="tile t7" style="left:599px;top:740px" role="img" aria-label="Painted portrait artwork"><span>Photographs,<br>Paintings &amp; Sculptures</span></div>
  <div class="tile t8" style="left:834px;top:740px" role="img" aria-label="Modern curved building at dusk"><span>Architectural Works</span></div>

  <div class="pledge">EVERY APPLICATION IS INDIVIDUALLY FILED AND MONITORED UNDER LAWYER SUPERVISION.</div>
  <div class="pledge-sub">PROTECT YOUR INTELLECTUAL PROPERTY RIGHTS</div>

  <div class="feature" style="left:124px">
    <h3><svg width="20" height="20" viewBox="0 0 20 20"><circle cx="10" cy="10" r="8.5" fill="none" stroke="#0a6fc9" stroke-width="1.8"/><path d="M13 7.2a4 4 0 1 0 0 5.6" fill="none" stroke="#0a6fc9" stroke-width="1.8"/></svg>COPYRIGHT CATEOGRIES</h3>
    <p>Lorem ipsum dolor sit amet, consectetuer adipiscing elit, sed diam nonummy nibh euismod tincidunt ut laoreet dolore ...</p>
  </div>
  <div class="feature" style="left:363px">
    <h3><svg width="26" height="22" viewBox="0 0 26 22"><rect x="6" y="1" width="9" height="5" transform="rotate(35 10 4)" fill="#0a6fc9"/><rect x="10" y="6" width="3" height="9" transform="rotate(-55 11 10)" fill="#0a6fc9"/><rect x="2" y="17" width="14" height="4" fill="#0a6fc9"/></svg>LAW &amp; STATUTES</h3>
    <p>Lorem ipsum dolor sit amet, consectetuer adipiscing elit, sed diam nonummy nibh euismod tincidunt ut laoreet dolore ...</p>
  </div>
  <div class="feature" style="left:597px">
    <h3><svg width="28" height="22" viewBox="0 0 28 22"><rect x="1.5" y="1.5" width="25" height="15" fill="none" stroke="#0a6fc9" stroke-width="2.5"/><rect x="11" y="17" width="6" height="3" fill="#0a6fc9"/><rect x="8" y="20" width="12" height="2" fill="#0a6fc9"/></svg>ABOUT US</h3>
    <p>Lorem ipsum dolor sit amet, consectetuer adipiscing elit, sed diam nonummy nibh euismod tincidunt ut laoreet dolore ...</p>
  </div>
  <div class="feature" style="left:830px">
    <h3><svg width="28" height="22" viewBox="0 0 28 22"><ellipse cx="16" cy="9" rx="11" ry="7" fill="#0a6fc9"/><ellipse cx="10" cy="12" rx="9" ry="6.5" fill="#0a6fc9" stroke="#f9f9f9" stroke-width="1.5"/><path d="M4 16l-2 5 7-3z" fill="#0a6fc9"/></svg>FAQs</h3>
    <p>Lorem ipsum dolor sit amet, consectetuer adipiscing elit, sed diam nonummy nibh euismod tincidunt ut laoreet dolore ...</p>
  </div>

  <footer class="footer">
    <div class="links">ABOUT US<span>|</span>CUSTOMER SERVICE<span>|</span>PRIVACY POLICY<span>|</span>CONTACT US<span>|</span>DISCLAIMER</div>
    <div class="copy">© 2013 Brightvaultly.com. All Rights Reserved.</div>
    <div class="social"><i></i><i></i></div>
  </footer>
</div>
</body>
</html>
```